Physician House Call Doctor

I need 2 newspaper color display adds. 1 small and 1 larger. I have attached some ideas but they need to be updated, more professional and eye-catching . I may also want to change the doctors picture and add some text. I need submit to newspaper in a PDF format and the adds must have a border.

```html
<!DOCTYPE html>
<html lang="en">
<head>
<meta charset="UTF-8">
<title>Physician House Calls Ad</title>
<link href="https://fonts.googleapis.com/css2?family=Arimo:wght@400;700&family=Tinos&display=swap" rel="stylesheet">
<style>
  :root {
    --navy: #1c3b6b;
    --navy-deep: #15305a;
    --sky: #3b8fd1;
    --pill: #2b8fd4;
    --ink: #1d2f4f;
    --white: #ffffff;
    --swoosh: #8a8f96;
    --photo-a: #5d86b5;
    --photo-b: #2f5b91;
    --portrait-a: #c9cfd6;
    --portrait-b: #8d9aa8;
  }
  * { margin: 0; padding: 0; box-sizing: border-box; }
  html, body { width: 932px; height: 1200px; overflow: hidden; background: #ececec; }
  .ad {
    position: relative;
    width: 932px; height: 1200px;
    background: var(--navy);
    padding: 34px;
    font-family: "Arimo", Arial, sans-serif;
  }
  .ad-inner {
    position: relative;
    width: 100%; height: 100%;
    background: var(--white);
    overflow: hidden;
  }
  .headline {
    position: absolute; top: 34px; left: 0; right: 0;
    text-align: center;
    color: var(--navy);
    font-weight: 700;
    font-size: 84px;
    line-height: 1.06;
    letter-spacing: -0.5px;
  }
  .doctor-line {
    position: absolute; top: 240px; left: 0; right: 0;
    text-align: center;
    font-family: "Tinos", "Times New Roman", serif;
    color: var(--sky);
    font-size: 54px;
    line-height: 1.15;
  }
  .benefits {
    position: absolute; top: 428px; left: 54px;
    list-style: none;
    color: var(--ink);
    font-size: 31px;
  }
  .benefits li { display: flex; align-items: center; margin-bottom: 18px; }
  .benefits svg { width: 34px; height: 34px; margin-right: 14px; flex: none; }
  .scene-photo {
    position: absolute; left: 0; right: 0; top: 680px; bottom: 0;
    background: linear-gradient(180deg, var(--photo-a) 0%, var(--photo-b) 60%, var(--navy-deep) 100%);
  }
  .swoosh { position: absolute; left: 0; top: 600px; width: 864px; height: 180px; }
  .portrait {
    position: absolute; left: 452px; right: 0; top: 640px;
    height: 400px;
    background: radial-gradient(ellipse at 50% 35%, var(--portrait-a) 0%, var(--portrait-b) 75%, var(--photo-b) 100%);
  }
  .brand {
    position: absolute; left: 54px; top: 850px;
    width: 380px;
    color: var(--white);
  }
  .brand-name {
    display: flex; align-items: center;
    font-weight: 700; font-size: 26px;
    white-space: nowrap;
  }
  .brand-name::before {
    content: ""; width: 20px; height: 20px; margin-right: 10px; flex: none;
    background: var(--white);
  }
  .credential {
    margin-top: 22px;
    font-size: 32px; line-height: 1.2;
  }
  .phone-pill {
    position: absolute; left: 140px; right: 34px; top: 1010px;
    height: 76px; border-radius: 38px;
    background: var(--pill);
    display: flex; align-items: center; justify-content: center;
    color: var(--white);
    font-weight: 700; font-size: 58px;
  }
  .phone-pill svg { width: 50px; height: 50px; margin-right: 20px; }
  .web {
    position: absolute; left: 0; right: 0; top: 1092px;
    text-align: center;
    color: var(--white);
    font-size: 27px;
    letter-spacing: 0.5px;
  }
</style>
</head>
<body>
  <div class="ad">
    <div class="ad-inner">
      <h1 class="headline">PHYSICIAN HOUSE<br>CALLS ARE BACK!</h1>
      <p class="doctor-line">Dr. Martin J Halvorsen<br>comes to your home !</p>

      <ul class="benefits">
        <li><svg viewBox="0 0 34 34"><circle cx="17" cy="17" r="14" fill="none" stroke="var(--navy)" stroke-width="3"/><path d="M10 17l5 5 10-11" fill="none" stroke="var(--navy)" stroke-width="3.5" stroke-linecap="round" stroke-linejoin="round"/></svg>Flu Shots now available!</li>
        <li><svg viewBox="0 0 34 34"><circle cx="17" cy="17" r="14" fill="none" stroke="var(--navy)" stroke-width="3"/><path d="M10 17l5 5 10-11" fill="none" stroke="var(--navy)" stroke-width="3.5" stroke-linecap="round" stroke-linejoin="round"/></svg>Why go out in the rain or snow?</li>
        <li><svg viewBox="0 0 34 34"><circle cx="17" cy="17" r="14" fill="none" stroke="var(--navy)" stroke-width="3"/><path d="M10 17l5 5 10-11" fill="none" stroke="var(--navy)" stroke-width="3.5" stroke-linecap="round" stroke-linejoin="round"/></svg>Medicare accepted for qualified patients.</li>
      </ul>

      <div class="scene-photo" role="img" aria-label="Soft blue photo of a residential building behind the doctor"></div>
      <svg class="swoosh" viewBox="0 0 864 180" preserveAspectRatio="none">
        <path d="M0 180 C 200 70, 480 30, 864 40 L864 0 L0 0 Z" fill="var(--white)"/>
        <path d="M0 170 C 200 62, 480 28, 864 36" fill="none" stroke="var(--swoosh)" stroke-width="12"/>
        <path d="M0 185 C 200 80, 480 44, 864 52" fill="none" stroke="var(--navy)" stroke-width="6" opacity="0.6"/>
      </svg>
      <div class="portrait" role="img" aria-label="Portrait photo of the doctor in a white coat with a stethoscope"></div>

      <div class="brand">
        <div class="brand-name">Riverline Home Medical</div>
        <p class="credential">Board Certified<br>Family Practice</p>
      </div>

      <div class="phone-pill">
        <svg viewBox="0 0 50 50"><circle cx="25" cy="25" r="21" fill="none" stroke="var(--white)" stroke-width="4"/><path d="M18 14c2 0 3 4 3 5s-2 2-2 3c1 3 4 6 7 7 1 0 2-2 3-2s5 1 5 3-2 5-5 5c-8-1-15-8-16-16 0-3 3-5 5-5z" fill="var(--white)"/></svg>
        202-555-0147
      </div>
      <p class="web">www.riverlinehomemed.com</p>
    </div>
  </div>
</body>
</html>
```